Etiketten-Design für eigene Eierverpackung im Bereich Freiland
Zielgruppe
Wir sind Großhändler in der Eierverpackungsbranche, unsere Zielgruppe sind Eierproduzenten
Aufgabenstellung
Wir suchen nach einem Etikett für eine eigene Eierverpackung im Bereich Freiland

```html
<!DOCTYPE html>
<html lang="de">
<head>
<meta charset="utf-8">
<title>Aus Freilandhaltung – Etikett</title>
<link href="https://fonts.googleapis.com/css2?family=Barlow:wght@700;800&display=swap" rel="stylesheet">
<style>
  :root {
    --green: #0b8a3b;
    --paper: #ffffff;
    --backdrop: #f4f4f2;
    --frame: #3a3a3a;
    --egg-light: #f6f6f6;
    --egg-shade: #d4d4d4;
    --letter-on-egg: #f2f2f2;
    --grass-light: #e9f2d8;
    --grass-mid: #9cc45a;
    --grass-deep: #4f8f2a;
  }
  * { box-sizing: border-box; margin: 0; padding: 0; }
  html, body {
    width: 848px; height: 1200px; overflow: hidden;
    background: var(--backdrop);
  }
  .label {
    position: absolute; left: 164px; top: 45px;
    width: 520px; height: 1110px;
    background: var(--paper);
    border: 1.5px solid var(--frame);
    overflow: hidden;
    font-family: "Barlow", "Arial Narrow", sans-serif;
    font-weight: 800;
    color: var(--green);
  }
  .egg-photo {
    position: absolute; left: 324px; top: 72px;
    width: 170px; height: 257px;
    background: linear-gradient(135deg, var(--egg-light) 0%, var(--egg-shade) 100%);
  }
  .headline { position: absolute; left: 40px; line-height: 1; white-space: nowrap; }
  .headline--aus { top: 72px; font-size: 34px; letter-spacing: 2px; }
  .headline--frei { top: 113px; font-size: 158px; letter-spacing: 44px; }
  .headline--frei .on-egg { color: var(--letter-on-egg); text-shadow: 2px 2px 4px rgba(0,0,0,.25); }
  .headline--land { top: 300px; font-size: 158px; letter-spacing: 6px; }
  .headline--haltung { top: 492px; font-size: 92px; letter-spacing: 6px; }
  .meadow {
    position: absolute; left: 0; top: 600px;
    width: 100%; height: 510px;
    background: linear-gradient(180deg, var(--paper) 0%, var(--grass-light) 35%, var(--grass-mid) 70%, var(--grass-deep) 100%);
  }
  .free-range-badge {
    position: absolute; left: 198px; top: 946px;
    width: 126px; height: 126px; border-radius: 50%;
    background: var(--green);
  }
</style>
</head>
<body>
  <div class="label">
    <div class="egg-photo" role="img" aria-label="Foto eines weißen Eis hinter dem Wort Frei"></div>

    <div class="headline headline--aus">AUS</div>
    <div class="headline headline--frei">FR<span class="on-egg">EI</span></div>
    <div class="headline headline--land">LAND</div>
    <div class="headline headline--haltung">HALTUNG</div>

    <div class="meadow" role="img" aria-label="Foto von hohen Wiesengräsern und Gräserrispen"></div>

    <div class="free-range-badge" role="img" aria-label="Siegel Freilandhaltung"></div>
  </div>
</body>
</html>
```